Business card design for new brand

We have recently rebranded and need a new business card template.

We are an insurance underwriting agency. All of our products are sold via other partner companies, so these are just to pass on our details to other organisations.

We would like to see designs that use the colour green (current stationary generally uses lime green (rgb 142,190,63) and forest green (0,154,79) to comply with our logo's colours. We are happy with other shades of green.

Business cards need to include our logo, as well as space for:
1. Full name
2. Qualifications (optional)
3. Title
4. Office number
5. Mobile number
6. Email address

Our logo is enclosed here.

```html
<!DOCTYPE html>
<html lang="en">
<head>
<meta charset="utf-8">
<title>Verdance Cover – Business Card</title>
<link rel="stylesheet" href="https://fonts.googleapis.com/css2?family=Open+Sans:wght@400;600;700&display=swap">
<style>
  :root {
    --forest: #009a4f;
    --lime: #8ebe3f;
    --ink: #1a1a1a;
    --muted: #555555;
    --paper: #ffffff;
    --card-dark: #121212;
    --backdrop: #3b3b3b;
  }
  * { box-sizing: border-box; margin: 0; padding: 0; }
  html, body { width: 1200px; height: 801px; overflow: hidden; }
  body {
    background: var(--backdrop);
    font-family: "Open Sans", Arial, sans-serif;
    display: flex;
    align-items: center;
    justify-content: center;
    gap: 60px;
  }
  .card {
    width: 520px;
    height: 297px;
    position: relative;
    overflow: hidden;
    border-bottom: 3px solid var(--forest);
    box-shadow: 0 10px 30px rgba(0,0,0,.35);
  }
  .card--front { background: var(--paper); display: flex; align-items: center; }
  .card--back { background: var(--card-dark); display: flex; align-items: center; justify-content: center; }

  .brand { display: flex; align-items: center; gap: 9px; }
  .brand__mark { width: 16px; height: 16px; background: var(--forest); flex: none; }
  .brand__name { font-weight: 600; color: var(--ink); font-size: 19px; letter-spacing: .2px; white-space: nowrap; }
  .card--front .brand { width: 300px; padding: 0 22px; justify-content: center; flex: none; }
  .card--back .brand { gap: 12px; }
  .card--back .brand__name { color: var(--paper); font-size: 34px; }
  .card--back .brand__mark { width: 28px; height: 28px; }

  .divider { width: 1px; height: 110px; background: var(--forest); flex: none; }

  .contact { padding-left: 18px; }
  .contact__name { color: var(--forest); font-weight: 700; font-size: 17px; letter-spacing: .4px; text-transform: uppercase; white-space: nowrap; }
  .contact__title { color: var(--muted); font-size: 12px; margin-bottom: 8px; }
  .contact__list { list-style: none; }
  .contact__item { display: flex; align-items: center; gap: 7px; color: var(--muted); font-size: 12px; line-height: 19px; white-space: nowrap; }
  .contact__icon { width: 10px; height: 10px; flex: none; }
</style>
</head>
<body>
  <section class="card card--front">
    <div class="brand">
      <span class="brand__mark"></span>
      <span class="brand__name">Verdance Cover Pty Ltd</span>
    </div>
    <div class="divider"></div>
    <div class="contact">
      <p class="contact__name">Daniel Carver</p>
      <p class="contact__title">President</p>
      <ul class="contact__list">
        <li class="contact__item">
          <svg class="contact__icon" viewBox="0 0 10 10"><path d="M2 1 L4 3 L3 4 Q4 6 6 7 L7 6 L9 8 L8 9 Q3 9 1 2 Z" fill="var(--lime)"/></svg>
          555-310-2184
        </li>
        <li class="contact__item">
          <svg class="contact__icon" viewBox="0 0 10 10"><rect x="2.5" y="0.5" width="5" height="9" rx="1" fill="none" stroke="var(--muted)"/></svg>
          555-310-2184
        </li>
        <li class="contact__item">
          <svg class="contact__icon" viewBox="0 0 10 10"><rect x="0.5" y="2" width="9" height="6" fill="var(--lime)"/><path d="M0.5 2 L5 5.5 L9.5 2" fill="none" stroke="#fff"/></svg>
          info@verdancecover.com
        </li>
        <li class="contact__item">
          <svg class="contact__icon" viewBox="0 0 10 10"><circle cx="5" cy="5" r="4.5" fill="var(--lime)"/><path d="M0.5 5 H9.5 M5 0.5 Q2.5 5 5 9.5 M5 0.5 Q7.5 5 5 9.5" fill="none" stroke="#fff" stroke-width=".7"/></svg>
          www.verdancecover.com
        </li>
      </ul>
    </div>
  </section>

  <section class="card card--back">
    <div class="brand">
      <span class="brand__mark"></span>
      <span class="brand__name">Verdance Cover Pty Ltd</span>
    </div>
  </section>
</body>
</html>
```